SEO AND WEB DESIGN COMPANY BUSINESS CARD DESIGN

I need an eye catching , simple business card design that will match my logo . I need 2 versions of it ( white background and black background) - SOME PEOPLE DID NOT GET IT AND SENDING US FRONT WHITE BACK WHITE VERSIONS WHICH IS NOT CORRECT.

ONE VERSION SHOULD BE BACK AND FRONT ALL BLACK , SECOND VERSION SHOULD BE BACK AND FRONT ALL WHITE

logo psd files are attached for both versions. The business card is going to have : First Name- Last name - position - phone numbers

```html
<!DOCTYPE html>
<html lang="en">
<head>
<meta charset="utf-8">
<title>Business Card – Dark Version</title>
<link rel="stylesheet" href="https://fonts.googleapis.com/css2?family=Lato:wght@300;400&display=swap">
<style>
  :root {
    --backdrop: #d5d5d5;
    --card-light: #4b4a4c;
    --card-dark: #2d2b2d;
    --accent: #3a9fd2;
    --accent-deep: #3a7db6;
    --ink-light: #f2f2f2;
    --ink-soft: #d8d8d8;
  }
  * { box-sizing: border-box; margin: 0; padding: 0; }
  html, body {
    width: 1033px;
    height: 1200px;
    overflow: hidden;
    background: var(--backdrop);
    font-family: "Lato", sans-serif;
  }
  .sheet {
    position: relative;
    width: 1033px;
    height: 1200px;
  }
  .card {
    position: absolute;
    left: 158px;
    width: 727px;
    height: 415px;
    background: linear-gradient(110deg, var(--card-light) 0%, var(--card-dark) 100%);
    overflow: hidden;
  }
  .card--front { top: 145px; }
  .card--back { top: 634px; }
  .card__band {
    position: absolute;
    left: 0;
    bottom: 0;
    width: 100%;
    height: 17px;
    background: linear-gradient(90deg, var(--accent), var(--accent-deep));
  }
  .holder {
    position: absolute;
    left: 46px;
    top: 80px;
  }
  .holder__name {
    font-weight: 400;
    font-size: 45px;
    line-height: 1;
    color: var(--ink-light);
  }
  .holder__role {
    margin-top: 6px;
    font-weight: 400;
    font-size: 21px;
    letter-spacing: 2.5px;
    color: var(--accent);
  }
  .contacts {
    position: absolute;
    left: 32px;
    top: 286px;
    list-style: none;
  }
  .contacts__item {
    display: flex;
    align-items: center;
    height: 26px;
    font-weight: 300;
    font-size: 16.5px;
    letter-spacing: 0.6px;
    color: var(--ink-soft);
  }
  .contacts__icon {
    width: 19px;
    height: 19px;
    margin-right: 12px;
    flex: none;
  }
  .brand {
    position: absolute;
    left: 0;
    right: 0;
    top: 178px;
    text-align: center;
    font-weight: 400;
    font-size: 50px;
    letter-spacing: 2px;
    line-height: 1;
    color: var(--ink-light);
  }
</style>
</head>
<body>
<main class="sheet">

  <section class="card card--front" aria-label="Card front">
    <div class="holder">
      <p class="holder__name">Your Name</p>
      <p class="holder__role">POSITION</p>
    </div>

    <ul class="contacts">
      <li class="contacts__item">
        <svg class="contacts__icon" viewBox="0 0 20 20" aria-hidden="true">
          <circle cx="10" cy="10" r="10" fill="var(--accent)"/>
          <rect x="7" y="4.5" width="6" height="11" rx="1.2" fill="none" stroke="#2f2e30" stroke-width="1.6"/>
        </svg>
        012 2345 5678
      </li>
      <li class="contacts__item">
        <svg class="contacts__icon" viewBox="0 0 20 20" aria-hidden="true">
          <circle cx="10" cy="10" r="10" fill="var(--accent)"/>
          <path d="M6.2 5.2l2 -.4 1.2 2.6 -1.3 1.1c.6 1.4 1.6 2.4 3 3l1.1 -1.3 2.6 1.2 -.4 2c-4.6.3 -8.5 -3.6 -8.2 -8.2z" fill="#2f2e30"/>
        </svg>
        012 2345 5678
      </li>
      <li class="contacts__item">
        <svg class="contacts__icon" viewBox="0 0 20 20" aria-hidden="true">
          <circle cx="10" cy="10" r="10" fill="var(--accent)"/>
          <rect x="5" y="6.5" width="10" height="7.5" rx="1" fill="none" stroke="#2f2e30" stroke-width="1.5"/>
          <path d="M5.5 7l4.5 3.6 4.5 -3.6" fill="none" stroke="#2f2e30" stroke-width="1.5"/>
        </svg>
        youremail@email.com
      </li>
    </ul>

    <div class="card__band"></div>
  </section>

  <section class="card card--back" aria-label="Card back">
    <p class="brand">Northlane Digital</p>
    <div class="card__band"></div>
  </section>

</main>
</body>
</html>
```